Business Card Design Project

I have a newly designed logo (by Marlo through Artwork Hive) and now need a business card concept / design.

We are an HR consulting firm.

I am hoping that someone can advise me if they are able to see the logo that I chose in my last project (logo design) or if I need to upload that logo here in this project?

Obviously I want the business card to fit with the logo!

Industry/Entity Type

Business

```html
<!DOCTYPE html>
<html lang="en">
<head>
<meta charset="utf-8">
<title>Lorton Consulting – Business Cards</title>
<link rel="stylesheet" href="https://fonts.googleapis.com/css2?family=Open+Sans:wght@400;600;700&display=swap">
<style>
  :root {
    --page-bg: #d9d9d9;
    --card-black: #0c0c0c;
    --card-white: #f7f8f8;
    --brand-teal: #1ba3d6;
    --brand-green: #5cb83a;
    --accent-blue: #1fa6e2;
    --text-dark: #1d1d1d;
    --text-light: #ffffff;
    --text-muted: #6c6c6c;
  }
  * { margin: 0; padding: 0; box-sizing: border-box; }
  html, body { width: 1200px; height: 951px; overflow: hidden; }
  body {
    background: var(--page-bg);
    font-family: "Open Sans", Arial, sans-serif;
    position: relative;
  }
  .card {
    position: absolute;
    width: 560px;
    height: 340px;
    border-radius: 22px;
    overflow: hidden;
  }
  .card-front { left: 90px; top: 80px; background: var(--card-black); }
  .card-back  { left: 550px; top: 520px; background: var(--card-white); }

  .brand { position: absolute; display: flex; align-items: center; gap: 14px; }
  .brand-mark {
    width: 70px; height: 70px; border-radius: 50%;
    border: 4px solid var(--brand-teal); flex: none;
  }
  .brand-name {
    font-weight: 700; font-size: 38px; letter-spacing: -0.5px;
    color: var(--brand-teal); line-height: 1; white-space: nowrap;
  }
  .brand-tagline {
    font-size: 11.5px; font-weight: 600; color: var(--brand-green);
    margin-top: 4px; letter-spacing: 0.2px; white-space: nowrap;
  }
  .card-front .brand { left: 40px; top: 110px; }
  .card-front .brand-tagline { color: var(--brand-teal); }
  .front-web {
    position: absolute; left: 170px; top: 270px;
    color: var(--text-light); font-size: 17px; letter-spacing: 1.5px;
  }

  .back-swoosh { position: absolute; inset: 0; }
  .card-back .brand {
    left: 24px; top: 30px; flex-direction: column; gap: 8px; align-items: center;
  }
  .card-back .brand-mark { width: 60px; height: 60px; }
  .card-back .brand-name { font-size: 32px; }
  .card-back .brand-tagline { font-size: 10px; color: var(--text-muted); margin-top: 2px; }

  .contact-list { position: absolute; left: 30px; top: 226px; list-style: none; }
  .contact-item {
    display: flex; align-items: center; gap: 10px;
    font-size: 15px; color: var(--text-dark); line-height: 24px;
  }
  .contact-item svg { width: 14px; height: 14px; flex: none; }
  .web-accent { color: var(--accent-blue); }

  .holder {
    position: absolute; left: 400px; top: 150px; width: 150px;
    text-align: center; color: var(--text-light);
  }
  .holder-name { font-size: 19px; font-weight: 600; letter-spacing: 0.3px; }
  .holder-title { font-size: 13px; margin-top: 2px; }
</style>
</head>
<body>
  <section class="card card-front" aria-label="Card front">
    <div class="brand">
      <span class="brand-mark" aria-hidden="true"></span>
      <div>
        <div class="brand-name">Lorton Consulting</div>
        <div class="brand-tagline">Human Resources and Recruitment Solutions</div>
      </div>
    </div>
    <div class="front-web">www.lortonconsulting.com</div>
  </section>

  <section class="card card-back" aria-label="Card back">
    <svg class="back-swoosh" viewBox="0 0 560 340" preserveAspectRatio="none" aria-hidden="true">
      <path d="M360 0 C395 90 385 230 320 340 L340 340 C400 230 410 90 378 0 Z" fill="#111"/>
      <path d="M378 0 C410 90 400 230 340 340 L560 340 L560 0 Z" fill="var(--accent-blue)"/>
    </svg>
    <div class="brand">
      <span class="brand-mark" aria-hidden="true"></span>
      <div>
        <div class="brand-name">Lorton Consulting</div>
        <div class="brand-tagline">Human Resources and Recruitment Solutions</div>
      </div>
    </div>
    <ul class="contact-list">
      <li class="contact-item">
        <svg viewBox="0 0 16 16" aria-hidden="true"><path d="M4 1 L6.5 4 L5 6 C6 8.5 7.5 10 10 11 L12 9.5 L15 12 L13 15 C6.5 14.5 1.5 9.5 1 3 Z" fill="var(--accent-blue)"/></svg>
        041 2876 553
      </li>
      <li class="contact-item">
        <svg viewBox="0 0 16 16" aria-hidden="true"><rect x="1" y="3" width="14" height="10" rx="1.5" fill="var(--accent-blue)"/><path d="M1.5 4 L8 9 L14.5 4" stroke="#fff" stroke-width="1.3" fill="none"/></svg>
        maren@lortonconsulting.com.au
      </li>
      <li class="contact-item">
        <svg viewBox="0 0 16 16" aria-hidden="true"><circle cx="8" cy="8" r="7" fill="var(--accent-blue)"/></svg>
        <span>www.<span class="web-accent">lortonconsulting</span>.com.au</span>
      </li>
    </ul>
    <div class="holder">
      <div class="holder-name">Maren Lorton</div>
      <div class="holder-title">Director</div>
    </div>
  </section>
</body>
</html>
```